I'm looking for a smart new design for business cards

Industry/Entity Type

Commercial Electrical

Contact Information for Business Card

Logo, name, email, position, website QR

Requirements
Nice to have
• Logo embedded behind the text side

```html
<!DOCTYPE html>
<html lang="en">
<head>
<meta charset="UTF-8">
<title>Voltline Commercial – Business Card</title>
<link href="https://fonts.googleapis.com/css2?family=Rubik:wght@400;800&display=swap" rel="stylesheet">
<style>
  :root {
    --navy: #26297a;
    --red: #e0202c;
    --card: #ffffff;
    --backdrop: #e6e7ea;
    --card-shadow: rgba(20, 24, 40, 0.18);
  }
  * { box-sizing: border-box; margin: 0; padding: 0; }
  html, body {
    width: 1200px; height: 1200px; overflow: hidden;
    background: var(--backdrop);
    font-family: "Rubik", sans-serif;
  }
  .canvas {
    width: 1200px; height: 1200px;
    display: flex; flex-direction: column;
    align-items: center; justify-content: center; gap: 70px;
  }
  .card {
    position: relative;
    width: 720px; height: 412px;
    background: var(--card);
    border-radius: 34px;
    box-shadow: 0 12px 30px var(--card-shadow);
    overflow: hidden;
  }
  .brand-name {
    font-weight: 800;
    color: var(--navy);
    text-transform: uppercase;
    letter-spacing: 1px;
    line-height: 1.05;
    display: flex; align-items: center; gap: 14px;
  }
  .brand-mark {
    width: 22px; height: 22px; background: var(--red); flex: none;
  }
  /* front side */
  .card-front .brand-name {
    position: absolute; left: 50%; top: 128px;
    transform: translateX(-50%);
    font-size: 44px;
  }
  .card-front .web {
    position: absolute; left: 112px; bottom: 62px;
    font-size: 30px; color: var(--navy); font-weight: 400;
  }
  /* back side */
  .card-back .brand-name {
    position: absolute; left: 48px; top: 84px;
    font-size: 30px;
  }
  .card-back .divider {
    position: absolute; left: 330px; top: 62px;
    width: 3px; height: 288px; background: var(--red);
  }
  .details {
    position: absolute; left: 370px; top: 66px; right: 30px;
  }
  .person-name {
    font-weight: 800; font-size: 64px; color: var(--navy); line-height: 1;
  }
  .person-role {
    font-weight: 800; font-size: 34px; color: var(--red);
    margin-top: 4px; margin-bottom: 26px;
  }
  .contact-list { list-style: none; }
  .contact-item {
    display: flex; align-items: center; gap: 12px;
    font-size: 22px; color: var(--navy); margin-bottom: 10px;
  }
  .contact-item svg { width: 22px; height: 22px; flex: none; }
</style>
</head>
<body>
<main class="canvas">
  <section class="card card-front">
    <div class="brand-name"><span class="brand-mark"></span><span>Voltline<br>Commercial</span></div>
    <p class="web">www.voltlineco.com</p>
  </section>

  <section class="card card-back">
    <div class="brand-name"><span class="brand-mark"></span><span>Voltline<br>Commercial</span></div>
    <div class="divider"></div>
    <div class="details">
      <h1 class="person-name">Name</h1>
      <p class="person-role">CEO</p>
      <ul class="contact-list">
        <li class="contact-item">
          <svg viewBox="0 0 24 24" fill="none" stroke="var(--red)" stroke-width="2"><rect x="6" y="2" width="12" height="20" rx="2"/><line x1="11" y1="18" x2="13" y2="18"/></svg>
          <span>( 000 ) 555 0142</span>
        </li>
        <li class="contact-item">
          <svg viewBox="0 0 24 24" fill="var(--red)"><path d="M6.6 10.8a15 15 0 0 0 6.6 6.6l2.2-2.2a1 1 0 0 1 1-.25 11.4 11.4 0 0 0 3.6.57 1 1 0 0 1 1 1V20a1 1 0 0 1-1 1A17 17 0 0 1 3 4a1 1 0 0 1 1-1h3.5a1 1 0 0 1 1 1c0 1.25.2 2.45.57 3.57a1 1 0 0 1-.25 1z"/></svg>
          <span>( 000 ) 555 0142</span>
        </li>
        <li class="contact-item">
          <svg viewBox="0 0 24 24" fill="none" stroke="var(--red)" stroke-width="2"><rect x="2" y="5" width="20" height="14" rx="1"/><polyline points="2,5 12,13 22,5"/></svg>
          <span>hello@voltlineco.com</span>
        </li>
        <li class="contact-item">
          <svg viewBox="0 0 24 24" fill="none" stroke="var(--red)" stroke-width="2"><circle cx="12" cy="12" r="10"/><ellipse cx="12" cy="12" rx="4.5" ry="10"/><line x1="2" y1="12" x2="22" y2="12"/></svg>
          <span>www.voltlineco.com</span>
        </li>
      </ul>
    </div>
  </section>
</main>
</body>
</html>
```